Book Cover Design Project - SIMPLE ART, Pre-Concepted

We already have a full design concept for the cover art. It is however in a low quality word document format. This project is to recreate existing example guideline art in as much vector art possible for great quality print production. Artistic flare is welcome. This will be for a book cover (front/back) and I want the quality to be excellent.

Art to be provided in Adobe Illustrator format. The book will be 6wide x 9high, so the artboard for the cover needs to be set up to 12.5 wide x 9 high with .125" bleeds.

Copy content for the spine: "Beneath the Orchard Lamps at Dusk" RL Ombrisko.

Here is a link to download the word document "template" and a new photo for the back page. I'm not sure that I like the new photo, it is possible the old one in the word document will work.

www.kelmarpressworks.com/uploads/BriefingFilesSetAll.zip

I've got a fast deadline on this project because the client would like to have manufacturing completed by Christmas...which is why this is only a 2 day project. I appreciate your interest in our project.

Gordon

Try this link...seems I was missing the .zip extension which may have been causing problems.

Requirements
Must have
• Adobe Illustrator Files
CMYK color setup - no color definitions for project
Artboard Size: 12.625 wide x 9.125 high
Art Orientation: Flat image should have the back book page on the left side, front page on the right side, spine copy running down the middle.

```html
<!DOCTYPE html>
<html lang="en">
<head>
<meta charset="utf-8">
<title>Beneath the Orchard Lamps at Dusk – Book Cover</title>
<link href="https://fonts.googleapis.com/css2?family=Oswald:wght@300;400;600;700&family=Pathway+Gothic+One&display=swap" rel="stylesheet">
<style>
  :root {
    --cover-grey: #a3a8b0;
    --cover-grey-light: #b4b8be;
    --ink: #111111;
    --spine-red: #c5222b;
    --cross-black: #000000;
    --photo-dark: #3a2a24;
    --photo-warm: #c47a4e;
  }
  * { margin: 0; padding: 0; box-sizing: border-box; }
  html, body { width: 1200px; height: 864px; overflow: hidden; background: var(--cover-grey); }
  .cover {
    position: relative; width: 1200px; height: 864px;
    background: var(--cover-grey); overflow: hidden; color: var(--ink);
  }
  .author-photo {
    position: absolute; left: 11px; top: 13px; width: 207px; height: 249px;
    background: linear-gradient(160deg, var(--photo-warm) 0%, #8a5a40 45%, var(--photo-dark) 100%);
  }
  .about-heading {
    position: absolute; left: 230px; top: 0; font-family: "Oswald", sans-serif;
    font-weight: 700; font-size: 46px; line-height: 60px; letter-spacing: -0.5px;
  }
  .about-intro {
    position: absolute; left: 230px; top: 62px; width: 300px;
    font-family: "Oswald", sans-serif; font-weight: 600; font-size: 18px; line-height: 29px;
  }
  .about-intro span { display: block; white-space: nowrap; }
  .about-body {
    position: absolute; left: 10px; top: 279px; width: 540px;
    font-family: "Pathway Gothic One", sans-serif; font-size: 15.5px; line-height: 19.1px;
  }
  .about-body span { display: block; white-space: nowrap; }
  .spine-title {
    position: absolute; left: 576px; top: 432px; width: 860px;
    transform: translate(-50%, -50%) rotate(90deg);
    font-family: "Oswald", sans-serif; font-weight: 400; font-size: 21px;
    color: var(--spine-red); text-align: center; white-space: nowrap; letter-spacing: 0.3px;
  }
  .front-art { position: absolute; left: 0; top: 0; }
  .front-text {
    position: absolute; left: 660px; width: 510px; text-align: center;
    font-family: "Oswald", sans-serif; font-weight: 400; color: var(--spine-red);
    white-space: nowrap; letter-spacing: 0.5px;
  }
  .front-title { top: 584px; font-size: 29px; }
  .front-subtitle { top: 670px; font-size: 30px; }
  .front-author { top: 757px; font-size: 30px; }
</style>
</head>
<body>
<main class="cover">
  <section class="back-cover">
    <div class="author-photo" role="img" aria-label="Portrait photograph of the author in a dark suit and tie"></div>
    <h2 class="about-heading">About the author:</h2>
    <p class="about-intro">
      <span>The word of God says that “I know the</span>
      <span>plans I have for you” (Jeremiah 29:11)</span>
      <span>and that “before I formed you in the</span>
      <span>womb I knew you” (Jeremiah 1:15).</span>
      <span>These verses of scripture depict the</span>
      <span>&nbsp;life of&nbsp; Rowan L Ombrisko</span>
    </p>
    <p class="about-body">
      <span>As a little boy Rowan was always told that he was going to be a preacher.</span>
      <span>The magnitude of this repeated statement and exactly what it entailed was not</span>
      <span>taken seriously or truly understood, at that time.&nbsp; It was not Rowan’s plan or desire</span>
      <span>to be a preacher, and he tried to do anything and everything to avoid the talks of him</span>
      <span>becoming one.&nbsp; Rowan’s path of life, although he believed in God, took him down the road</span>
      <span>that led him away from God.&nbsp; His struggles with life’s events and being an introvert</span>
      <span>kept him emotionally troubled, in a state of depression and wanting to commit suicide.</span>
      <span>Yet, as the Lord was with Jeremiah, even so was the Lord with Rowan.&nbsp; The Lord was to</span>
      <span>show Rowan just what it meant to have complete trust in Him and to know that He</span>
      <span>would always provide a way of an escape.&nbsp; Before Rowan came to the point of carrying</span>
      <span>out his plans to commit suicide, he prayed a simple prayer that God would give him a</span>
      <span>new family.&nbsp; At that exact moment Rowan’s life began to take a new direction.&nbsp; He began</span>
      <span>to seek after the Lord; it became his quest to find out what it meant to be a servant</span>
      <span>of God.&nbsp; Because of his being an introvert, he began to write his emotions on paper in</span>
      <span>the form of poems.&nbsp; Those poems gave him the strength to come out of depression</span>
      <span>and began his two year journey to find God.</span>
      <span>Rowan’s relationship with Jesus and salvation journey began at the age of nineteen.</span>
      <span>The poetry writing started as a therapeutic remedy for his troubled past, but</span>
      <span>developed into the psalms of Rowan because of God’s grace and mercy that delivered</span>
      <span>him from despair and hopelessness.</span>
      <span>God’s favor covers Rowan’s life and carries him from day to day.&nbsp; It is written</span>
      <span>that “without me (Christ) ye can do nothing” (John 15:5).&nbsp; This scripture resonates</span>
      <span>in Rowan’s heart.&nbsp; For, he truly believes that God is the author and he is just the</span>
      <span>vessel used of God.&nbsp; His desire is that each poem will be taken personally and</span>
      <span>become a tool used by everyone to help them on their Christian journey and</span>
      <span>to let them know that they are never alone in their experience and quest to be</span>
      <span>closer to the Lord Jesus Christ.</span>
    </p>
  </section>

  <div class="spine-title">Beneath the Orchard Lamps at Dusk: A Compilation of Poems by RL Ombrisko</div>

  <section class="front-cover">
    <svg class="front-art" width="1200" height="864" viewBox="0 0 1200 864" aria-hidden="true">
      <g class="cross-shadow" fill="var(--cover-grey-light)" opacity="0.85" transform="translate(820 690) rotate(-38)">
        <rect x="-190" y="-34" width="330" height="68"/>
        <rect x="20" y="-130" width="68" height="245"/>
      </g>
      <g class="cross" fill="var(--cross-black)">
        <rect x="971" y="40" width="85" height="477"/>
        <rect x="855" y="144" width="309" height="73"/>
      </g>
    </svg>
    <h1 class="front-text front-title">Beneath the Orchard Lamps at Dusk</h1>
    <p class="front-text front-subtitle">A Compliation of Poems</p>
    <p class="front-text front-author">RL Ombrisko</p>
  </section>
</main>
</body>
</html>
```